TARPLOAD business card design

TARPLOAD is a manufacturer of skip bags supplying both the domestic and commercial market. We wish to convey core characteristics of strength, professionalism and reliability to our customers. We are after a business card that uses our company colours of black and yellow as well as incorporating our logo. Our customers are predominantly in the construction or hardware industry. It is important the cards are professional as we are a small company wishing to appear larger than we actually are. more info on the company and product available at www.tarpload-example.com.au

Target Market(s)

hardware buyers, contruction company owners

Industry/Entity Type

Construction

Requirements
Must have
• company colours of black and yellow - No other colours or variation of yellow black. our company logo. card design must convey "tough"
• Card design must be landscape
• Details to be included on the card are:
• Name and Tiltle
• Phone number : 1300 41 62 53
• Mobile: 0452 718 903
• Fax: 03 9617 4852
• email: dale.hendry@tarpload-example.com.au
• address: PO Box 517, Kelvindale, VIC,3294
• Text in white when on a black background
Nice to have
• I like the idea of the back of the card being black with lighter circle area in the middle with black logo in the centre. Similar to the attached "iconic" card

```html
<!DOCTYPE html>
<html lang="en">
<head>
<meta charset="utf-8">
<title>TARPLOAD business card – front and back</title>
<link rel="stylesheet" href="https://fonts.googleapis.com/css2?family=Carlito:wght@400;700&display=swap">
<style>
  :root {
    --page: #ffffff;
    --ink: #000000;
    --gold: #f9c95c;
    --watermark: #e2e2e2;
    --icon-dark: #2b2118;
    --icon-gold: #e0b256;
    --band-light: #c9a35a;
    --band-dark: #4a3a22;
  }
  * { margin: 0; padding: 0; box-sizing: border-box; }
  html, body {
    width: 927px; height: 1200px; overflow: hidden;
    background: var(--page);
    font-family: "Carlito", "Calibri", sans-serif;
  }
  .sheet { position: relative; width: 927px; height: 1200px; }
  .card {
    position: absolute; left: 90px; width: 742px; height: 417px;
    border: 1.5px solid var(--ink); background: var(--page); overflow: hidden;
  }
  .card--front { top: 143px; }
  .card--back { top: 585px; }

  .brand-mark {
    position: absolute; color: var(--watermark); font-weight: 700;
    letter-spacing: 1px; line-height: 1; display: flex; align-items: center; gap: 10px;
  }
  .brand-mark__square { width: 0.7em; height: 0.7em; background: var(--watermark); }
  .card--front .brand-mark { left: 52px; top: 96px; font-size: 38px; }
  .card--back .brand-mark {
    left: 50%; top: 50%; transform: translate(-50%, -50%); font-size: 52px;
  }

  .person { position: absolute; right: 20px; top: 44px; text-align: right; }
  .person__name { color: var(--gold); font-size: 44px; line-height: 1; font-weight: 400; }
  .person__title { color: var(--ink); font-size: 22px; line-height: 1; margin-top: 14px; }

  .contact-list {
    position: absolute; left: 327px; top: 236px; list-style: none;
  }
  .contact-list__item {
    display: flex; align-items: center; height: 21px;
    font-size: 18px; color: var(--ink);
  }
  .contact-list__icon { width: 38px; height: 22px; flex: none; margin-right: 2px; }

  .footer-band { position: absolute; left: 0; right: 0; bottom: 0; height: 29px; }
  .footer-band__solid {
    position: absolute; left: 2px; top: 0; bottom: 0; width: 259px; background: var(--ink);
  }
  .footer-band__texture {
    position: absolute; left: 267px; right: 0; top: 0; bottom: 0;
    background: linear-gradient(180deg, var(--band-dark), var(--band-light) 45%, var(--band-dark));
  }
</style>
</head>
<body>
<main class="sheet">
  <section class="card card--front" aria-label="Card front">
    <div class="brand-mark"><span class="brand-mark__square"></span>TARPLOAD</div>

    <header class="person">
      <h1 class="person__name">Dale Hendry</h1>
      <p class="person__title">Managing Director</p>
    </header>

    <ul class="contact-list">
      <li class="contact-list__item">
        <svg class="contact-list__icon" viewBox="0 0 38 22" aria-hidden="true">
          <ellipse cx="19" cy="11" rx="18" ry="10.5" fill="var(--icon-dark)"/>
          <path d="M19 4a4 4 0 0 1 4 4c0 3-4 9-4 9s-4-6-4-9a4 4 0 0 1 4-4z" fill="var(--icon-gold)"/>
          <circle cx="19" cy="8" r="1.5" fill="var(--icon-dark)"/>
        </svg>PO Box 517, Kelvindale, VIC,3294
      </li>
      <li class="contact-list__item">
        <svg class="contact-list__icon" viewBox="0 0 38 22" aria-hidden="true">
          <ellipse cx="19" cy="11" rx="18" ry="10.5" fill="var(--icon-dark)"/>
          <path d="M11 9c0-3 16-3 16 0v2h-4V9h-8v2h-4z" fill="var(--icon-gold)"/>
          <rect x="13" y="11" width="12" height="6" rx="1" fill="var(--icon-gold)"/>
        </svg>1300 41 62 53
      </li>
      <li class="contact-list__item">
        <svg class="contact-list__icon" viewBox="0 0 38 22" aria-hidden="true">
          <ellipse cx="19" cy="11" rx="18" ry="10.5" fill="var(--icon-dark)"/>
          <rect x="15" y="3" width="8" height="16" rx="1.5" fill="var(--icon-gold)"/>
          <rect x="16.5" y="5" width="5" height="5" fill="var(--icon-dark)"/>
        </svg>0452 718 903
      </li>
      <li class="contact-list__item">
        <svg class="contact-list__icon" viewBox="0 0 38 22" aria-hidden="true">
          <ellipse cx="19" cy="11" rx="18" ry="10.5" fill="var(--icon-dark)"/>
          <rect x="14" y="4" width="10" height="5" fill="var(--icon-gold)"/>
          <rect x="11" y="9" width="16" height="7" rx="1" fill="var(--icon-gold)"/>
          <rect x="14" y="14" width="10" height="3" fill="var(--icon-dark)"/>
        </svg>03 9617 4852
      </li>
      <li class="contact-list__item">
        <svg class="contact-list__icon" viewBox="0 0 38 22" aria-hidden="true">
          <ellipse cx="19" cy="11" rx="18" ry="10.5" fill="var(--icon-dark)"/>
          <rect x="11" y="6" width="16" height="10" fill="var(--icon-gold)"/>
          <path d="M11 6l8 6 8-6" fill="none" stroke="var(--icon-dark)" stroke-width="1.3"/>
        </svg>dale.hendry@tarpload-example.com.au
      </li>
    </ul>

    <div class="footer-band">
      <div class="footer-band__solid"></div>
      <div class="footer-band__texture" role="img" aria-label="Gold and brown diagonal striped texture band"></div>
    </div>
  </section>

  <section class="card card--back" aria-label="Card back">
    <div class="brand-mark"><span class="brand-mark__square"></span>TARPLOAD</div>
  </section>
</main>
</body>
</html>
```